Heritage Hollow Business Cards

Require a business card design. <br/><br/>Needs to include logo (either round or long version) plus these details:<br/>Maya Torvel<br/>Heritage Hollow<br/>maya@quonbrook.com.au<br/>02 6481 7390<br/>PO Box Glenwarra NSW 2913<br/>www.heritagehollow.com.au<br/><br/>I need in an editable format so that I can create for multiple staff members. <br/><br/>

Target Market(s)

We are an online store selling renovation products to home owners are builders. Looking for a classic classy design.

Industry/Entity Type

Home And Garden

Contact Information for Business Card

Maya Torvel
Heritage Hollow
maya@quonbrook.com.au
02 6481 7390
PO Box Glenwarra NSW 2913
www.heritagehollow.com.au

Colors

Designer to choose colors to be used in the design.

Requirements
Must have
• Must include Logo.

```html
<!DOCTYPE html>
<html lang="en">
<head>
<meta charset="utf-8">
<title>Heritage Hollow Business Cards</title>
<link rel="stylesheet" href="https://fonts.googleapis.com/css2?family=Lora:wght@400;500&display=swap">
<style>
  :root {
    --page-bg: #e6e3de;
    --card-bg: #ffffff;
    --ink: #1f1f1f;
    --ink-soft: #2c2c2c;
    --rule: #1a1a1a;
    --shadow: rgba(0, 0, 0, 0.18);
  }
  * { margin: 0; padding: 0; box-sizing: border-box; }
  html, body {
    width: 1189px;
    height: 1200px;
    overflow: hidden;
    background: var(--page-bg);
    font-family: "Lora", Georgia, serif;
    color: var(--ink);
  }
  .canvas { position: relative; width: 1189px; height: 1200px; }
  .card {
    position: absolute;
    left: 169px;
    width: 851px;
    background: var(--card-bg);
    border-radius: 26px;
    box-shadow: 0 6px 18px var(--shadow);
  }
  .card--front { top: 112px; height: 472px; }
  .card--back { top: 641px; height: 486px; }

  .wordmark {
    position: absolute;
    font-family: "Lora", Georgia, serif;
    font-weight: 500;
    font-size: 52px;
    line-height: 1;
    color: var(--ink);
    white-space: nowrap;
  }
  .card--front .wordmark { left: 91px; top: 136px; }
  .card--back .wordmark { left: 0; right: 0; top: 248px; text-align: center; }

  .person { position: absolute; left: 53px; top: 256px; }
  .person__name { font-size: 26px; font-weight: 500; line-height: 1.2; }
  .person__title { font-size: 20px; line-height: 1.4; color: var(--ink-soft); }

  .divider {
    position: absolute;
    left: 53px; top: 333px;
    width: 740px; height: 0;
    border-top: 1.5px solid var(--rule);
  }

  .contacts { position: absolute; left: 53px; top: 356px; list-style: none; }
  .contacts li {
    display: flex; align-items: center; gap: 9px;
    height: 28.5px;
    font-size: 20px; color: var(--ink-soft);
  }
  .contacts svg { width: 22px; height: 22px; flex: none; }

  .address {
    position: absolute; right: 55px; top: 356px;
    text-align: right; font-size: 20px; line-height: 28.5px;
    font-style: normal; color: var(--ink-soft);
  }
</style>
</head>
<body>
<main class="canvas">
  <section class="card card--front" aria-label="Business card front">
    <div class="wordmark">Heritage Hollow</div>

    <div class="person">
      <div class="person__name">Maya Torvel</div>
      <div class="person__title">Managing Director</div>
    </div>

    <div class="divider"></div>

    <ul class="contacts">
      <li>
        <svg viewBox="0 0 22 22" aria-hidden="true">
          <circle cx="11" cy="11" r="10" fill="none" stroke="#1f1f1f" stroke-width="1.4"/>
          <path d="M8 6.2c.6-.4 1.2-.2 1.5.4l.8 1.6c.2.5 0 1-.4 1.3l-.6.4c.5 1.3 1.4 2.3 2.6 3l.5-.5c.4-.4.9-.5 1.4-.2l1.4.9c.5.3.6 1 .2 1.5l-.7.8c-.7.7-2 .7-3.3-.1-2.2-1.3-3.9-3.4-4.5-5.8-.3-1.4 0-2.7 1.1-3.3z" fill="#1f1f1f"/>
        </svg>
        <span>02 6481 7390</span>
      </li>
      <li>
        <svg viewBox="0 0 22 22" aria-hidden="true">
          <circle cx="11" cy="11" r="10" fill="none" stroke="#1f1f1f" stroke-width="1.4"/>
          <rect x="5.5" y="7.5" width="11" height="7.5" rx="0.8" fill="#1f1f1f"/>
          <path d="M5.8 8l5.2 4 5.2-4" fill="none" stroke="#fff" stroke-width="1"/>
        </svg>
        <span>maya@quonbrook.com.au</span>
      </li>
      <li>
        <svg viewBox="0 0 22 22" aria-hidden="true">
          <circle cx="11" cy="11" r="10" fill="none" stroke="#1f1f1f" stroke-width="1.4"/>
          <circle cx="11" cy="11" r="6.5" fill="#1f1f1f"/>
          <g fill="none" stroke="#fff" stroke-width="0.7">
            <ellipse cx="11" cy="11" rx="2.8" ry="6.5"/>
            <line x1="4.5" y1="11" x2="17.5" y2="11"/>
            <line x1="5.5" y1="8" x2="16.5" y2="8"/>
            <line x1="5.5" y1="14" x2="16.5" y2="14"/>
          </g>
        </svg>
        <span>www.heritagehollow.com.au</span>
      </li>
    </ul>

    <address class="address">PO Box Glenwarra<br>NSW 2913</address>
  </section>

  <section class="card card--back" aria-label="Business card back">
    <div class="wordmark">Heritage Hollow</div>
  </section>
</main>
</body>
</html>
```